NFC (Near field communication) - Business Card Design

IT/ Telecom:

We would like a new business card that contains our logo, contact info for the company and contact info for the owner. We also wolud like to be innovative, and create NFC technology inside the card.

This means that mobile phones can be placed on the card, and the contactinfo automaticly stores into the phonebook. Therefore, a cirkle or similar - with the text: "Place your phone here!" (please write it in Norwagian): "Aktiver NFC og legg mobilen din her!".

Please google NFC or near field communication and use your imagination on the design as we love surprises :-)

Industry/Entity Type

Communication

Requirements
Must have
• Text: "Activate NFC on your phone and place your mobile here - in Norwegian: "Aktiver NFC og legg mobilen din her!".
Nice to have
• Please see attachment #5 for inspiration.

```html
<!DOCTYPE html>
<html lang="no">
<head>
<meta charset="utf-8">
<title>Linkvera – NFC visittkort</title>
<link rel="stylesheet" href="https://fonts.googleapis.com/css2?family=Open+Sans:ital,wght@0,400;0,600;0,700;1,400;1,600&family=Lato:wght@400;700&display=swap">
<style>
  :root{
    --page:#e9eaec;
    --card:#ffffff;
    --brand:#3d7893;
    --brand-light:#5f9cb8;
    --ink:#1d1d1f;
    --muted:#b9bcbf;
    --arrow:#d3d6d9;
  }
  *{box-sizing:border-box;margin:0;padding:0}
  html,body{width:1200px;height:868px;overflow:hidden;background:var(--page)}
  body{position:relative;font-family:"Open Sans",Arial,sans-serif}

  .card{position:absolute;background:var(--card);overflow:hidden;box-shadow:0 10px 28px rgba(0,0,0,.18)}

  /* Back: NFC side */
  .card-nfc{left:125px;top:159px;width:340px;height:550px}
  .nfc-arrow{position:absolute;left:147px;top:58px;width:46px;height:40px}
  .nfc-spot{position:absolute;left:150px;top:218px;width:40px;height:32px;border-radius:50%;background:var(--brand)}
  .nfc-hint{position:absolute;left:0;right:0;top:272px;text-align:center;font-style:italic;font-weight:600;font-size:15px;line-height:19px;color:var(--muted)}
  .nfc-band{position:absolute;left:0;right:0;bottom:0;height:108px;background:linear-gradient(90deg,var(--brand),var(--brand-light));display:flex;align-items:center;padding-left:34px;gap:14px}
  .mark{width:54px;height:42px;border-radius:8px}
  .nfc-band .mark{background:#fff}
  .brand-name{font-family:"Open Sans",Arial,sans-serif;font-weight:400;font-size:38px;letter-spacing:-.5px;line-height:1}
  .nfc-band .brand-name{color:#fff}

  /* Front: contact side */
  .card-front{left:525px;top:264px;width:550px;height:340px}
  .front-logo{position:absolute;left:36px;top:38px;display:flex;align-items:center;gap:14px}
  .front-logo .mark{background:var(--brand)}
  .front-logo .brand-name{color:var(--brand)}
  .contact{position:absolute;left:32px;top:118px;list-style:none;font-size:14px;line-height:18px;color:var(--ink)}
  .contact li{display:flex;align-items:flex-start;gap:12px;font-weight:600}
  .contact li.address{margin-bottom:2px}
  .contact svg{width:14px;height:14px;margin-top:2px;flex:none;fill:var(--brand)}
  .contact .gap{width:14px;flex:none}
  .person{position:absolute;right:40px;top:140px;text-align:right}
  .person-name{font-family:"Lato",Arial,sans-serif;font-size:30px;color:var(--brand);line-height:1.05}
  .person-role{font-family:"Open Sans",Arial,sans-serif;font-weight:700;font-size:16px;color:var(--ink)}
  .edge-pointer{position:absolute;right:0;top:140px;width:22px;height:36px}
  .front-band{position:absolute;left:0;top:0;width:550px;height:340px}
  .web{position:absolute;left:44px;bottom:32px;color:#fff;font-weight:700;font-size:19px}
</style>
</head>
<body>

<section class="card card-nfc" aria-label="NFC-side">
  <svg class="nfc-arrow" viewBox="0 0 46 40" aria-hidden="true">
    <polygon points="13,0 33,0 33,16 46,16 23,40 0,16 13,16" fill="var(--arrow)"/>
  </svg>
  <div class="nfc-spot"></div>
  <p class="nfc-hint">Aktiver NFC og legg<br>mobilen din her!</p>
  <div class="nfc-band">
    <span class="mark"></span>
    <span class="brand-name">linkvera</span>
  </div>
</section>

<section class="card card-front" aria-label="Kontaktside">
  <svg class="front-band" viewBox="0 0 550 340" aria-hidden="true">
    <defs>
      <linearGradient id="bandFill" x1="0" x2="1" y1="0" y2="0">
        <stop offset="0" stop-color="#3d7893"/>
        <stop offset="1" stop-color="#5f9cb8"/>
      </linearGradient>
    </defs>
    <polygon points="0,228 550,300 550,340 0,340" fill="url(#bandFill)"/>
  </svg>

  <div class="front-logo">
    <span class="mark"></span>
    <span class="brand-name">linkvera</span>
  </div>

  <ul class="contact">
    <li class="address">
      <svg viewBox="0 0 14 14"><path d="M7 0a5 5 0 0 0-5 5c0 3.6 5 9 5 9s5-5.4 5-9a5 5 0 0 0-5-5zm0 7a2 2 0 1 1 0-4 2 2 0 0 1 0 4z"/></svg>
      <span>Address line 1<br>Address line 2</span>
    </li>
    <li>
      <svg viewBox="0 0 14 14"><path d="M4 0h6a1 1 0 0 1 1 1v12a1 1 0 0 1-1 1H4a1 1 0 0 1-1-1V1a1 1 0 0 1 1-1zm0 2v9h6V2zm3 10a.8.8 0 1 0 0-.01z"/></svg>
      <span>+47 00 000 000</span>
    </li>
    <li>
      <svg viewBox="0 0 14 14"><path d="M3 0h8v4H3zM1 5h12a1 1 0 0 1 1 1v5h-3v3H3v-3H0V6a1 1 0 0 1 1-1zm3 5v3h6v-3z"/></svg>
      <span>+47 00 000 000</span>
    </li>
    <li>
      <svg viewBox="0 0 14 14"><path d="M0 3h14v1L7 8 0 4zm0 2.2 7 4 7-4V11H0z"/></svg>
      <span>ola.nord@linkvera.com</span>
    </li>
  </ul>

  <div class="person">
    <p class="person-name">Ola Nordvik</p>
    <p class="person-role">programer</p>
  </div>
  <svg class="edge-pointer" viewBox="0 0 22 36" aria-hidden="true">
    <polygon points="22,0 0,18 22,36" fill="var(--arrow)"/>
  </svg>

  <p class="web">www.linkvera.rs</p>
</section>

</body>
</html>
```